Business Cards for Internet Security Company

Awesome designers! This is the opportunity to help design cards for a forward thinking network security company. They use threat information gathered from peer groups to make intelligent decisions on what threats are relevant and which arent. ( not that you need this to do designs, but just so you know where they are coming from. ) :-)

We'd like to see a two side design and the deliverables will be in illustrator 4. The logo is attached and the logo colors are attached in the JPG and I've attached a an eps of the logo and icon

```html
<!DOCTYPE html>
<html lang="en">
<head>
<meta charset="utf-8">
<title>Corvane Business Cards</title>
<link rel="stylesheet" href="https://fonts.googleapis.com/css2?family=Open+Sans:wght@400;600;700&display=swap">
<style>
  :root {
    --bg: #27bdec;
    --navy: #1d4f7c;
    --navy-deep: #17416a;
    --steel: #2f6790;
    --brand-blue: #2a73b8;
    --text-navy: #1b4a78;
    --white: #ffffff;
    --pattern-light: #d9e8f5;
  }
  * { box-sizing: border-box; margin: 0; padding: 0; }
  html, body {
    width: 1200px; height: 900px; overflow: hidden;
    background: var(--bg);
    font-family: "Open Sans", Arial, sans-serif;
  }
  .card {
    position: absolute; left: 250px; width: 700px; height: 400px;
    overflow: hidden;
    box-shadow: 0 10px 24px rgba(0, 40, 80, 0.35);
  }
  .card-back {
    top: 35px;
    background: linear-gradient(110deg, var(--navy-deep) 0%, var(--navy) 55%, var(--steel) 100%);
    color: var(--white);
    display: flex; flex-direction: column; align-items: center; justify-content: center;
  }
  .brand { display: flex; align-items: center; gap: 14px; font-weight: 600; letter-spacing: 0.5px; }
  .brand-dot { border-radius: 50%; flex: none; }
  .card-back .brand { font-size: 64px; line-height: 1; }
  .card-back .brand-dot { width: 44px; height: 44px; background: var(--white); }
  .tagline { margin-top: 14px; text-align: center; font-size: 15px; line-height: 1.35; letter-spacing: 0.3px; }

  .card-front { top: 465px; background: var(--white); }
  .front-art { position: absolute; inset: 0; }
  .card-front .brand { position: absolute; left: 36px; top: 38px; font-size: 58px; line-height: 1; color: var(--brand-blue); }
  .card-front .brand-dot { width: 40px; height: 40px; background: var(--brand-blue); }
  .person { position: absolute; left: 40px; top: 160px; color: var(--text-navy); }
  .person-name { font-size: 22px; font-weight: 700; }
  .person-role { font-size: 16px; margin-top: 2px; }
  .contacts { position: absolute; left: 40px; top: 226px; list-style: none; color: var(--text-navy); }
  .contacts li { display: flex; align-items: center; gap: 10px; font-size: 17px; height: 24px; }
  .contacts svg { width: 16px; height: 16px; flex: none; }
  .address-band {
    position: absolute; left: 0; right: 0; bottom: 0; height: 46px;
    background: var(--navy); color: var(--pattern-light);
    display: flex; align-items: center; gap: 10px; padding-left: 40px; font-size: 17px;
  }
  .address-band svg { width: 14px; height: 18px; }
</style>
</head>
<body>
  <section class="card card-back">
    <div class="brand"><span class="brand-dot"></span>Corvane</div>
    <p class="tagline">Coordinated Cyber Defense<br>Let's see where we land!</p>
  </section>

  <section class="card card-front">
    <svg class="front-art" viewBox="0 0 700 400" preserveAspectRatio="none">
      <defs>
        <linearGradient id="swoosh" x1="0" y1="0" x2="1" y2="1">
          <stop offset="0" stop-color="#1d4f7c"/>
          <stop offset="1" stop-color="#3a6f97"/>
        </linearGradient>
      </defs>
      <path d="M420 0 L700 0 L700 400 L0 400 L0 354 L600 318 C520 230 450 120 420 0 Z" fill="url(#swoosh)"/>
      <path d="M500 0 L700 0 L700 220 L640 210 C580 160 520 90 500 0 Z" fill="var(--pattern-light)" role="img" aria-label="Decorative blue scale pattern"/>
    </svg>

    <div class="brand"><span class="brand-dot"></span>Corvane</div>

    <div class="person">
      <p class="person-name">Liam Hartley</p>
      <p class="person-role">Chief Executive Officer | Co-Founder</p>
    </div>

    <ul class="contacts">
      <li><svg viewBox="0 0 16 16"><rect width="16" height="16" rx="3" fill="#2a73b8"/><rect x="5" y="3" width="6" height="10" rx="1" fill="#fff"/></svg>0412558310</li>
      <li><svg viewBox="0 0 16 16"><rect width="16" height="16" rx="3" fill="#2a73b8"/><path d="M4 4c1 4 4 7 8 8l1-2-2-1-1 1c-2-1-3-2-4-4l1-1-1-2z" fill="#fff"/></svg>+61240007315</li>
      <li><svg viewBox="0 0 16 16"><rect width="16" height="16" rx="3" fill="#2a73b8"/><rect x="3" y="5" width="10" height="7" fill="#fff"/><path d="M3 5l5 4 5-4" stroke="#2a73b8" fill="none"/></svg>hello@corvane.com</li>
      <li><svg viewBox="0 0 16 16"><rect width="16" height="16" rx="3" fill="#2a73b8"/><circle cx="8" cy="8" r="4.5" fill="none" stroke="#fff"/><path d="M3.5 8h9M8 3.5v9" stroke="#fff"/></svg>www.corvane.com</li>
    </ul>

    <div class="address-band">
      <svg viewBox="0 0 14 18"><path d="M7 0a6 6 0 0 1 6 6c0 5-6 12-6 12S1 11 1 6a6 6 0 0 1 6-6z" fill="#d9e8f5"/><circle cx="7" cy="6" r="2.2" fill="#1d4f7c"/></svg>
      Unit 4/12 Harlow Lane, Merewether Newcastle NSW 2291
    </div>
  </section>
</body>
</html>
```